【概要】 住宅会社様の完成見学会のバナー制作です。 Web広告で使用するためのバナーデザインを募集します。 【依頼内容】 ・サイズ: 横1200× 縦628px、横1080× 縦1080px ・作成数: 1種類 ・利用用途:SNS広告(facebook/Instagram) 【目的】 完成見学会の来場促進(ぺージは下記) https://harubel.co.jp/ie/news/ie-news-8412-2-2-2-2-3-2-2-2-2-2-2-2/ 【デザインイメージ】 ・ターゲット層:30代~40代前半の主婦(若め)子供ができたばかり。旦那は普通の会社員。 ・雰囲気:お任せします 【使用素材】 添付のものをお使い下さい(全て使用しなくて結構です) ※開催日ですが、11/20.21は終了しているので削除し、残りの日程をバナーに表記してください。 【参考(クライアント)サイト】 https://harubel.co.jp https://sukanemo.com 【契約金額(税抜)】 3,000円/デザイン 最終納品のファイル形式は、AIもしくはPSDデータとしますが、デザイン提出段階では、PDFもしくはJPEGで問題ありません。 その他ご質問等ありましたら、気軽にお問い合わせください。 ご応募をお待ちしております! |

```html
<!DOCTYPE html>
<html lang="ja">
<head>
<meta charset="utf-8">
<title>完成見学会 OPEN HOUSE</title>
<link rel="stylesheet" href="https://fonts.googleapis.com/css2?family=Montserrat:wght@800&family=Noto+Serif+JP:wght@500;700&display=swap">
<style>
  :root {
    --tan: #c6a47e;
    --maroon: #8c3f31;
    --date-brown: #9a4a38;
    --white: #ffffff;
    --ink: #2a2320;
  }
  * { margin: 0; padding: 0; box-sizing: border-box; }
  html, body { width: 1200px; height: 628px; overflow: hidden; }
  body { font-family: "Noto Serif JP", serif; }
  .banner { position: relative; width: 1200px; height: 628px; background: var(--tan); overflow: hidden; }

  .photo { position: absolute; }
  .photo-exterior { left: 0; top: 0; width: 610px; height: 196px; background: linear-gradient(180deg, #c9d6e4 0%, #b7b5b0 55%, #d8d4cc 100%); }
  .photo-living { left: 620px; top: 0; width: 200px; height: 196px; background: linear-gradient(160deg, #eee8df 0%, #a27451 60%, #6f4a32 100%); }
  .photo-entrance { left: 828px; top: 0; width: 312px; height: 196px; background: linear-gradient(90deg, #5b6470 0%, #8a5a3b 45%, #a06b45 60%, #c9ccd0 100%); }
  .photo-side { left: 1148px; top: 0; width: 52px; height: 196px; background: linear-gradient(180deg, #aeb8c2, #8f8f8c); }
  .photo-study { left: 620px; top: 436px; width: 580px; height: 192px; background: linear-gradient(100deg, #d9d3cb 0%, #b99366 45%, #6d7b8a 100%); }

  .headline {
    position: absolute; left: 14px; top: 116px;
    font-family: "Montserrat", sans-serif; font-weight: 800;
    font-size: 76px; letter-spacing: -1px; color: var(--white);
    text-shadow: 3px 4px 6px rgba(0,0,0,.45);
    line-height: 1;
  }

  .limited-badge {
    position: absolute; left: -6px; top: 196px; width: 212px; height: 212px;
    border-radius: 50%; background: var(--maroon); color: var(--white);
    display: flex; flex-direction: column; align-items: center; justify-content: center;
  }
  .limited-badge .period { font-size: 28px; font-weight: 500; line-height: 1.3; }
  .limited-badge .held { font-size: 52px; font-weight: 700; line-height: 1.2; letter-spacing: 2px; }

  .event-info {
    position: absolute; left: 300px; top: 214px; color: var(--white);
    font-size: 40px; font-weight: 500; line-height: 58px; letter-spacing: 1px;
  }

  .date-card { position: absolute; top: 208px; height: 212px; border: 3px solid var(--white); }
  .date-card.nov { left: 664px; width: 256px; }
  .date-card.dec { left: 940px; width: 262px; }
  .date-card svg { position: absolute; inset: 0; width: 100%; height: 100%; }
  .date-card .month { position: absolute; left: 16px; top: 8px; color: var(--white); font-size: 38px; font-weight: 500; }
  .date-card .weekday { position: absolute; left: 18px; top: 62px; color: var(--white); font-size: 20px; font-weight: 500; }
  .date-card .days { position: absolute; right: 26px; bottom: 22px; color: var(--date-brown); font-size: 38px; font-weight: 500; }

  .reservation-band { position: absolute; left: 296px; top: 454px; width: 316px; height: 52px; }
  .reservation-band svg { position: absolute; inset: 0; }
  .reservation-band span { position: absolute; right: 20px; top: 6px; color: var(--white); font-size: 28px; font-weight: 500; }

  .brand-block { position: absolute; left: 0; top: 502px; width: 612px; height: 126px; background: var(--white); }
  .brand-name { position: absolute; left: 18px; top: 44px; color: var(--ink); font-size: 38px; font-weight: 500; }
</style>
</head>
<body>
<main class="banner">
  <div class="photo photo-exterior" role="img" aria-label="完成した住宅の外観写真"></div>
  <div class="photo photo-living" role="img" aria-label="木の床とソファのあるリビングの写真"></div>
  <div class="photo photo-entrance" role="img" aria-label="木製ドアの玄関の写真"></div>
  <div class="photo photo-side" role="img" aria-label="住宅周辺の写真"></div>
  <div class="photo photo-study" role="img" aria-label="造作カウンターのある書斎スペースの写真"></div>

  <h1 class="headline">OPEN HOUSE</h1>

  <div class="limited-badge">
    <span class="period">3週間限定</span>
    <span class="held">開催</span>
  </div>

  <div class="event-info">
    <p>完成見学会</p>
    <p>10:00~17:30</p>
    <p>富山市赤田にて</p>
  </div>

  <div class="date-card nov">
    <svg viewBox="0 0 250 206" preserveAspectRatio="none"><polygon points="250,0 250,206 0,206" fill="#fff"/></svg>
    <span class="month">11月</span>
    <span class="weekday">土日</span>
    <span class="days">27,28</span>
  </div>
  <div class="date-card dec">
    <svg viewBox="0 0 256 206" preserveAspectRatio="none"><polygon points="256,0 256,206 0,206" fill="#fff"/></svg>
    <span class="month">12月</span>
    <span class="weekday">土日</span>
    <span class="days">4,5</span>
  </div>

  <div class="reservation-band">
    <svg width="316" height="52" viewBox="0 0 316 52"><polygon points="40,0 316,0 316,52 0,52" fill="#8c3f31"/></svg>
    <span>完全予約制</span>
  </div>

  <div class="brand-block">
    <p class="brand-name">harubel×SUKANEMO</p>
  </div>
</main>
</body>
</html>
```